Global Expert Network Firm needs business card design

We need business card design for a new company based in Seoul, South Korea called 'Corwell Insight Partners'. We recruit industry experts covering all countries and connect our client and recruited expert by phone, face-to-face meetings and etc. We are a global expert network firm that is focused on delivering high-quality experts to our clients throughout the world. Our clients include multinational corporations, global consulting firms, private equity firms, venture capital firms, asset management companies.
We have made new logo and please find attachment.(Please use new logo)
Target Market(s)
Global Consulting Firms, Investment Firms, Private Equity Firms, Venture Capital Firms.
Industry/Entity Type
Recruitment
Contact Information for Business Card
We need two Languages (English and Korean Version).
The front is Korean and the back is English version.
[The back] [English]
Company Name: Corwell Insight Partners, Inc.
CEO Name: Daniel Park
Address: #507, Hanbit Bldg, 82 Maebongsan-ro, Dobong-gu, Seoul, 01327, Korea
Tel. +82 2 718 4052
Fax. +82 2 864 1097
Mobile. +82 10 7264 8815
Email: daniel@corwellip.com
Web: www.corwellip.com
[The front] [Korean] => Described in same order as English version.
회사명: 코웰인사이트파트너스(주)
대표이사: 박도현
주소: 서울시 도봉구 매봉산로 82 한빛빌딩 507호
Tel. 02 718 4052
Fax. 02 864 1097
Mobile. 010 7264 8815
Web: www.corwellip.com
Look and feel
Each slider illustrates characteristics of the customer's brand and the style your logo design should communicate.

```html
<!DOCTYPE html>
<html lang="ko">
<head>
<meta charset="utf-8">
<title>Corwell Insight Partners — Business Cards</title>
<link rel="stylesheet" href="https://fonts.googleapis.com/css2?family=Montserrat:wght@400;600;700&family=Noto+Sans+KR:wght@400;700&display=swap">
<style>
  :root {
    --navy: #1e2350;
    --paper: #ffffff;
    --bg: #ffffff;
    --shadow: rgba(0, 0, 0, 0.28);
  }
  * { box-sizing: border-box; margin: 0; padding: 0; }
  html, body { width: 1200px; height: 1200px; overflow: hidden; background: var(--bg); }
  body { position: relative; font-family: "Montserrat", "Noto Sans KR", sans-serif; }

  .card {
    position: absolute;
    width: 584px;
    height: 334px;
    box-shadow: 2px 9px 14px var(--shadow);
  }
  .card--front { left: 236px; top: 239px; background: var(--paper); color: var(--navy); font-family: "Noto Sans KR", "Montserrat", sans-serif; }
  .card--back { left: 380px; top: 702px; background: var(--navy); color: var(--paper); }

  .brand {
    position: absolute;
    left: 412px; top: 38px;
    width: 135px; height: 135px;
    display: flex; flex-direction: column; justify-content: center;
    padding-left: 8px;
    font-family: "Montserrat", sans-serif;
    font-weight: 400;
    font-size: 17px;
    line-height: 1.6;
    letter-spacing: 0.02em;
    text-transform: uppercase;
  }
  .card--front .brand { background: var(--navy); color: var(--paper); }
  .card--back .brand { background: var(--paper); color: var(--navy); }

  .ruled { position: absolute; border-left: 2px solid currentColor; padding-left: 8px; }

  .identity { left: 37px; top: 138px; }
  .identity .name { font-weight: 700; font-size: 17px; line-height: 1.3; }
  .identity .role { font-size: 11px; line-height: 1.5; }
  .card--back .identity { top: 131px; }
  .card--back .identity .name { font-family: "Montserrat", sans-serif; font-size: 18px; letter-spacing: 0.04em; text-transform: uppercase; }
  .card--back .identity .role { font-size: 12px; }

  .contacts { left: 37px; top: 199px; list-style: none; font-family: "Montserrat", sans-serif; font-size: 11.5px; line-height: 18.4px; }
  .contacts .label { display: inline-block; width: 22px; font-weight: 700; }

  .company { left: 332px; top: 198px; font-size: 11.5px; line-height: 15px; }
  .company dt { font-weight: 700; font-size: 12.5px; line-height: 18px; }
  .company dd { margin-bottom: 4px; }

  .address { left: 322px; top: 218px; font-size: 11.5px; line-height: 18.4px; }
  .address .heading { font-weight: 700; font-size: 11px; letter-spacing: 0.03em; }
</style>
</head>
<body>

  <section class="card card--front" aria-label="Korean side">
    <div class="brand">Corwell<br>Insight<br>Partners</div>

    <div class="ruled identity">
      <p class="name">박도현</p>
      <p class="role">대표이사</p>
    </div>

    <ul class="ruled contacts">
      <li><span class="label">T :</span> +82 2 718 4052</li>
      <li><span class="label">M:</span> +82 10 7264 8815</li>
      <li><span class="label">F :</span> +82 2 864 1097</li>
      <li><span class="label">W:</span> www.corwellip.com</li>
      <li><span class="label">E :</span> daniel@corwellip.com</li>
    </ul>

    <dl class="ruled company">
      <dt>회사명</dt>
      <dd>코웰인사이트파트너스(주)</dd>
      <dt>주소</dt>
      <dd>서울시 도봉구 매봉산로<br>82 한빛빌딩 507호</dd>
    </dl>
  </section>

  <section class="card card--back" aria-label="English side">
    <div class="brand">Corwell<br>Insight<br>Partners</div>

    <div class="ruled identity">
      <p class="name">Daniel Park</p>
      <p class="role">CEO</p>
    </div>

    <ul class="ruled contacts">
      <li><span class="label">T :</span> +82 2 718 4052</li>
      <li><span class="label">M:</span> +82 10 7264 8815</li>
      <li><span class="label">F :</span> +82 2 864 1097</li>
      <li><span class="label">W:</span> www.corwellip.com</li>
      <li><span class="label">E :</span> daniel@corwellip.com</li>
    </ul>

    <div class="ruled address">
      <p class="heading">ADDRESS</p>
      <p>#507, Hanbit Bldg,<br>82 Maebongsan-ro<br>Dobong-gu, Seoul, 01327, Korea</p>
    </div>
  </section>

</body>
</html>
```